Print campaign

This project consist of producing a print campaign that ties into "personal skin care moments" and that will appeal to our target market (colored skinned women) to raise product awareness by creating a connection between the model and the Mavuri Brand.

This will entail 1 model portrayed in a very realistic manner taking care of her skin and demonstrating the appeal of being herself and loving herself (which is the tag line) because skin care matters to her. These "moments" will be done in a candid yet elegant style and in a manner where the viewer connects with the character in a way that they can say "yeah, me too" - and ultimately connect to the Mavuri Brand being their product of choice for a beautiful toned skin.

Dear designers,
I would like to make a small update in the direction of the is piece. The tag line does not have to be repeated because it is already on the actual jar instead can you use the following sentence: Lighten your skin in all safety OR Safely whiten your complexion.
 
Thanks,

V

```html
<!DOCTYPE html>
<html lang="en">
<head>
<meta charset="utf-8">
<title>Be Yourself Love Yourself</title>
<link rel="stylesheet" href="https://fonts.googleapis.com/css2?family=Inter:wght@900&display=swap">
<style>
  :root {
    --backdrop: #eef0f4;
    --skin-deep: #7a4a32;
    --skin-warm: #a96e4e;
    --braid-plum: #5a2340;
    --braid-magenta: #a8245e;
    --ink: #0b0b0b;
  }
  html, body {
    margin: 0;
    padding: 0;
    width: 1200px;
    height: 900px;
    overflow: hidden;
    background: var(--backdrop);
  }
  .campaign {
    position: relative;
    width: 1200px;
    height: 900px;
    overflow: hidden;
    background: var(--backdrop);
  }
  .model-portrait {
    position: absolute;
    left: 230px;
    top: 0;
    width: 970px;
    height: 900px;
    background:
      radial-gradient(ellipse 260px 330px at 820px 660px, var(--braid-plum) 0%, rgba(90,35,64,0.85) 55%, rgba(90,35,64,0) 100%),
      radial-gradient(ellipse 420px 300px at 520px 180px, var(--skin-warm) 0%, rgba(169,110,78,0.9) 50%, rgba(169,110,78,0) 100%),
      radial-gradient(ellipse 300px 420px at 680px 420px, var(--skin-deep) 0%, rgba(122,74,50,0.8) 55%, rgba(122,74,50,0) 100%),
      radial-gradient(ellipse 160px 360px at 920px 180px, var(--braid-magenta) 0%, rgba(168,36,94,0) 100%);
  }
  .tagline {
    position: absolute;
    left: 48px;
    top: 468px;
    margin: 0;
    font-family: "Inter", "Helvetica Neue", Arial, sans-serif;
    font-weight: 900;
    font-size: 108px;
    line-height: 97px;
    letter-spacing: -4px;
    color: var(--ink);
    text-transform: uppercase;
  }
  .tagline span { display: block; }
</style>
</head>
<body>
  <main class="campaign">
    <div class="model-portrait" role="img" aria-label="Woman with magenta box braids lying upside down on a white surface, eyes closed, hands resting on her chest and shoulder"></div>
    <h1 class="tagline">
      <span>Be</span>
      <span>Yourself</span>
      <span>Love</span>
      <span>Yourself</span>
    </h1>
  </main>
</body>
</html>
```